Website Re-design for Kids Playhouse Business

Need current website which looks very outdated to be re-designed to look modern and contemporary, reduce clutter significantly and make it look elegant and simple.
Current website: http://www.tinyforthouse.com.au/
A website which the business owner likes, use as reference/inspiration: http://vesk.com.au/
Looking for light green palette, natural colours. "WHAT'S ON" page/link no longer required.
Updates
Industry/Entity Type
Business
Number of Pages Required
5+ page
Look and feel
Each slider illustrates characteristics of the customer's brand and the style your logo design should communicate.

```html
<!DOCTYPE html>
<html lang="en">
<head>
<meta charset="utf-8">
<title>Tiny Fort House Roselands – Website Layouts</title>
<link href="https://fonts.googleapis.com/css2?family=Gelasio:wght@400&family=Montserrat:wght@500;700&family=Fredoka:wght@600&display=swap" rel="stylesheet">
<style>
:root{
  --stage:#ececec;
  --white:#ffffff;
  --ink:#2a2a2a;
  --muted:#555555;
  --red:#e0222a;
  --tan:#d8b7a5;
  --footer:#2b2a29;
  --footer-text:#d9d9d9;
  --serif:'Gelasio', Georgia, serif;
  --sans:'Montserrat', Arial, sans-serif;
  --display:'Fredoka', 'Arial Rounded MT Bold', sans-serif;
}
*{box-sizing:border-box;margin:0;padding:0}
html,body{width:1200px;height:2917px;overflow:hidden;background:var(--stage)}
.layout{position:absolute;background:var(--white);overflow:hidden;box-shadow:0 2px 14px rgba(0,0,0,.12)}
.desktop{left:25px;top:64px;width:813px;height:1611px}
.mobile{left:881px;top:152px;width:272px;height:2592px}
.abs{position:absolute}

/* hero */
.hero-photo{position:absolute;left:0;top:0;width:100%;background:linear-gradient(160deg,#b8ada7 0%,#d7cdc7 35%,#c9bfba 60%,#a99b93 100%)}
.brand{position:absolute;display:flex;align-items:center;gap:6px;padding:6px 9px;background:rgba(255,255,255,.92);font-family:var(--sans);font-weight:700;color:var(--red);text-transform:uppercase;letter-spacing:.5px}
.brand .mark{width:12px;height:12px;background:var(--red)}
.burger{position:absolute;width:22px}
.burger span{display:block;height:2px;background:#222;margin-bottom:4px}
.hero-title{position:absolute;left:0;width:100%;text-align:center;font-family:var(--display);color:var(--white);line-height:1}

/* text */
.copy{position:absolute;font-family:var(--serif);color:var(--ink)}
.copy p+p{margin-top:1.2em}
.more{position:absolute;font-family:var(--sans);font-weight:500;color:var(--ink);display:flex;align-items:center;gap:5px}
.arrow{display:inline-block}

/* card band */
.band{position:absolute;left:0;width:100%;background:var(--tan)}
.card-photo{position:absolute}
.photo-a{background:linear-gradient(135deg,#5a3d2f,#9a7a66 50%,#3f2b22)}
.photo-b{background:linear-gradient(135deg,#3c7a3a,#c23b5a 45%,#2f5fa0 75%,#6aa84f)}
.photo-c{background:linear-gradient(135deg,#2a6fb8,#3ab0d9 40%,#e0c23a 70%,#2f8a55)}
.card{position:absolute;background:var(--white);border-top:2px solid var(--red);padding:10px 9px}
.card .tag{font-family:var(--sans);font-weight:700;color:var(--red);text-transform:uppercase}
.card h3{font-family:var(--serif);font-weight:400;color:var(--ink);margin:7px 0 8px}
.card .sub{font-family:var(--sans);font-weight:500;color:var(--ink);text-transform:uppercase}
.card .text{font-family:var(--serif);color:var(--muted);margin-top:5px}
.card .arrow{margin-top:6px}
.dots{position:absolute;display:flex;gap:3px}
.dots span{width:7px;height:7px;border-radius:50%;border:1px solid var(--red)}
.dots span.on{background:var(--red)}

/* footer */
.footer{position:absolute;left:0;width:100%;background:var(--footer);color:var(--footer-text);font-family:var(--sans)}
.skyline{position:absolute;left:0;bottom:0;width:100%;background:linear-gradient(180deg,rgba(0,0,0,0),rgba(0,0,0,.45))}
.field{position:absolute;border-bottom:1px solid #8a8a8a;font-weight:500;color:var(--footer-text)}
.send{position:absolute;border:1px solid #bfbfbf;color:var(--white);font-weight:500;display:flex;align-items:center;justify-content:center}
.foot-head{position:absolute;font-weight:700;color:var(--white);text-transform:uppercase}
.foot-text{position:absolute;line-height:1.55}
.social{position:absolute;display:flex;gap:3px}
.social span{border-radius:50%;background:#e6e6e6}
</style>
</head>
<body>

<!-- Desktop layout -->
<section class="layout desktop" aria-label="Desktop home page">
  <div class="hero-photo" style="height:486px" role="img" aria-label="Photo of two children painting together at a bright kitchen table"></div>
  <div class="brand" style="left:115px;top:14px;font-size:13px"><span class="mark"></span>Tiny Fort House</div>
  <div class="burger" style="left:690px;top:48px"><span></span><span></span><span></span></div>
  <h1 class="hero-title" style="top:376px;font-size:118px;letter-spacing:2px">Roselands</h1>

  <div class="copy" style="left:167px;top:532px;width:520px;font-size:14.5px;line-height:23px">
    <p>Welcome to Tiny Fort House, Sydney's newest and best party &amp; play centre!</p>
    <p>Tiny Fort House is an indoor Kids Play Centre and Cafe that offers both kids and adults a chance to enjoy their time, together! We pride ourselves in offering the best indoor play centre for your kids to engage in fun and learning activities in a specially created environment...</p>
  </div>
  <div class="more" style="left:167px;top:686px;font-size:9px">More About
    <svg class="arrow" width="9" height="7" viewBox="0 0 9 7"><path d="M0 3.5h7M4.5 1l2.7 2.5L4.5 6" stroke="#e0222a" stroke-width="1.4" fill="none"/></svg></div>

  <div class="band" style="top:743px;height:464px"></div>

  <div class="card-photo photo-a" style="left:23px;top:802px;width:237px;height:158px" role="img" aria-label="Photo of girls at a birthday party table"></div>
  <div class="card" style="left:52px;top:940px;width:179px;height:176px">
    <div class="tag" style="font-size:7px">Perfect venue for</div>
    <h3 style="font-size:14px;line-height:19px">Birthdays And Private Parties</h3>
    <div class="sub" style="font-size:6.5px">How our birthday parties work</div>
    <div class="text" style="font-size:8.5px;line-height:12px">You will need a minimum of 10 children to have a party. Extra Children will be charged accordingly.</div>
    <svg class="arrow" width="9" height="7" viewBox="0 0 9 7"><path d="M0 3.5h7M4.5 1l2.7 2.5L4.5 6" stroke="#e0222a" stroke-width="1.4" fill="none"/></svg>
  </div>

  <div class="card-photo photo-b" style="left:288px;top:802px;width:237px;height:158px" role="img" aria-label="Photo of a colourful themed party room"></div>
  <div class="card" style="left:317px;top:940px;width:179px;height:176px">
    <div class="tag" style="font-size:7px">4 kids loving</div>
    <h3 style="font-size:14px;line-height:19px">Party Rooms Themes</h3>
    <div class="sub" style="font-size:6.5px">How our birthday parties work</div>
    <div class="text" style="font-size:8.5px;line-height:12px">Birthday venues for kids in Sydney, Childrens theme Party, Kids parties, Childrens birthday venue, Childrens parties, Kids Birthday...</div>
    <svg class="arrow" width="9" height="7" viewBox="0 0 9 7"><path d="M0 3.5h7M4.5 1l2.7 2.5L4.5 6" stroke="#e0222a" stroke-width="1.4" fill="none"/></svg>
  </div>

  <div class="card-photo photo-c" style="left:553px;top:802px;width:237px;height:158px" role="img" aria-label="Photo of children playing in a ball pit"></div>
  <div class="card" style="left:582px;top:940px;width:179px;height:176px">
    <div class="tag" style="font-size:7px">We host</div>
    <h3 style="font-size:14px;line-height:19px">School Holiday Programs</h3>
    <div class="sub" style="font-size:6.5px">Tiny Fort House - Roselands -</div>
    <div class="text" style="font-size:8.5px;line-height:12px">Tiny Fort House Playhouse &amp; Cafe Roselands - Spring School Holiday Program All activities are FREE, after initial...</div>
    <svg class="arrow" width="9" height="7" viewBox="0 0 9 7"><path d="M0 3.5h7M4.5 1l2.7 2.5L4.5 6" stroke="#e0222a" stroke-width="1.4" fill="none"/></svg>
  </div>

  <div class="dots" style="left:390px;top:1153px"><span class="on"></span><span></span><span></span><span></span></div>

  <div class="copy" style="left:167px;top:1257px;width:500px;font-size:14.5px;line-height:23px">
    <p>Excellent place for kids and parents, amazing party rooms, friendly, fun and helpful staff! I highly recommend for hosting your next party or just to relax in air-con whilst watching your kids have a ball on the play equipment and activities!</p>
  </div>
  <div class="more" style="left:167px;top:1368px;font-size:9px">Mia Rowe
    <svg class="arrow" width="9" height="7" viewBox="0 0 9 7"><path d="M0 3.5h7M4.5 1l2.7 2.5L4.5 6" stroke="#e0222a" stroke-width="1.4" fill="none"/></svg></div>

  <footer class="footer" style="top:1446px;height:165px">
    <div class="skyline" style="height:120px" role="img" aria-label="Silhouettes of jumping children in front of a city skyline"></div>
    <div class="field" style="left:107px;top:32px;width:110px;height:22px;font-size:8px">Name*</div>
    <div class="field" style="left:235px;top:32px;width:90px;height:22px;font-size:8px">Phone*</div>
    <div class="field" style="left:335px;top:32px;width:128px;height:22px;font-size:8px">Email*</div>
    <div class="field" style="left:477px;top:32px;width:120px;height:22px;font-size:8px">Message*</div>
    <div class="send" style="left:617px;top:22px;width:90px;height:30px;font-size:8.5px">Send Message</div>
    <div class="foot-head" style="left:107px;top:89px;font-size:8px">Postal Address</div>
    <div class="foot-text" style="left:107px;top:105px;font-size:7.5px">18 Wattle Lane<br>Roselands 2196 NSW<br>Australia</div>
    <div class="foot-text" style="left:226px;top:105px;font-size:7.5px">02 9000 1234<br>Email: hello@tinyforthouse.com.au</div>
    <div class="social" style="left:567px;top:104px"><span style="width:11px;height:11px"></span><span style="width:11px;height:11px"></span><span style="width:11px;height:11px"></span><span style="width:11px;height:11px"></span><span style="width:11px;height:11px"></span><span style="width:11px;height:11px"></span></div>
    <div class="foot-text" style="left:567px;top:124px;font-size:7.5px">© Copyright 2018 Tiny Fort House Roselands</div>
  </footer>
</section>

<!-- Mobile layout -->
<section class="layout mobile" aria-label="Mobile home page">
  <div class="hero-photo" style="height:432px" role="img" aria-label="Photo of two children painting together at a bright kitchen table"></div>
  <div class="brand" style="left:12px;top:22px;font-size:10px;padding:5px 7px"><span class="mark" style="width:9px;height:9px"></span>Tiny Fort House</div>
  <div class="burger" style="left:240px;top:52px"><span></span><span></span><span></span></div>
  <h1 class="hero-title" style="top:378px;font-size:50px">Roselands</h1>

  <div class="copy" style="left:12px;top:470px;width:250px;font-size:14px;line-height:22px">
    <p>Welcome to Tiny Fort House, Sydney's newest and best party &amp; play centre!</p>
    <p>Tiny Fort House is an indoor Kids Play Centre and Cafe that offers both kids and adults a chance to enjoy their time, together! We pride ourselves in offering the best indoor play centre for your kids to engage in fun and learning activities in a specially created environment...</p>
  </div>
  <div class="more" style="left:12px;top:732px;font-size:8px">More About
    <svg class="arrow" width="9" height="7" viewBox="0 0 9 7"><path d="M0 3.5h7M4.5 1l2.7 2.5L4.5 6" stroke="#e0222a" stroke-width="1.4" fill="none"/></svg></div>

  <div class="band" style="top:802px;height:1113px"></div>

  <div class="card-photo photo-a" style="left:17px;top:852px;width:241px;height:160px" role="img" aria-label="Photo of girls at a birthday party table"></div>
  <div class="card" style="left:46px;top:1003px;width:181px;height:125px;padding:8px 9px">
    <div class="tag" style="font-size:6.5px">Perfect venue for</div>
    <h3 style="font-size:13.5px;line-height:18px;margin:5px 0 6px">Birthdays And Private Parties</h3>
    <div class="sub" style="font-size:6px">How our birthday parties work</div>
    <div class="text" style="font-size:8px;line-height:11px">You will need a minimum of 10 children to have a party. Extra Children will be charged accordingly.</div>
    <svg class="arrow" width="9" height="7" viewBox="0 0 9 7"><path d="M0 3.5h7M4.5 1l2.7 2.5L4.5 6" stroke="#e0222a" stroke-width="1.4" fill="none"/></svg>
  </div>

  <div class="card-photo photo-b" style="left:17px;top:1198px;width:241px;height:160px" role="img" aria-label="Photo of a colourful themed party room"></div>
  <div class="card" style="left:46px;top:1350px;width:181px;height:122px;padding:8px 9px">
    <div class="tag" style="font-size:6.5px">4 kids loving</div>
    <h3 style="font-size:13.5px;line-height:18px;margin:5px 0 6px">Party Rooms Themes</h3>
    <div class="sub" style="font-size:6px">How our birthday parties work</div>
    <div class="text" style="font-size:8px;line-height:11px">Birthday venues for kids in Sydney, Childrens theme Party, Kids parties, Childrens birthday venue, Childrens parties, Kids Birthday...</div>
    <svg class="arrow" width="9" height="7" viewBox="0 0 9 7"><path d="M0 3.5h7M4.5 1l2.7 2.5L4.5 6" stroke="#e0222a" stroke-width="1.4" fill="none"/></svg>
  </div>

  <div class="card-photo photo-c" style="left:17px;top:1544px;width:241px;height:160px" role="img" aria-label="Photo of children playing in a ball pit"></div>
  <div class="card" style="left:46px;top:1696px;width:181px;height:130px;padding:8px 9px">
    <div class="tag" style="font-size:6.5px">We host</div>
    <h3 style="font-size:13.5px;line-height:18px;margin:5px 0 6px">School Holiday Programs</h3>
    <div class="sub" style="font-size:6px">Tiny Fort House - Roselands -</div>
    <div class="text" style="font-size:8px;line-height:11px">Tiny Fort House Playhouse &amp; Cafe Roselands - Spring School Holiday Program All activities are FREE, after initial...</div>
    <svg class="arrow" width="9" height="7" viewBox="0 0 9 7"><path d="M0 3.5h7M4.5 1l2.7 2.5L4.5 6" stroke="#e0222a" stroke-width="1.4" fill="none"/></svg>
  </div>

  <div class="copy" style="left:12px;top:1950px;width:252px;font-size:14px;line-height:22px">
    <p>Excellent place for kids and parents, amazing party rooms, friendly, fun and helpful staff! I highly recommend for hosting your next party or just to relax in air-con whilst watching your kids have a ball on the play equipment and activities!</p>
  </div>
  <div class="more" style="left:12px;top:2143px;font-size:8px">Mia Rowe
    <svg class="arrow" width="9" height="7" viewBox="0 0 9 7"><path d="M0 3.5h7M4.5 1l2.7 2.5L4.5 6" stroke="#e0222a" stroke-width="1.4" fill="none"/></svg></div>

  <footer class="footer" style="top:2199px;height:393px">
    <div class="skyline" style="height:170px" role="img" aria-label="Silhouettes of jumping children in front of a city skyline"></div>
    <div class="field" style="left:12px;top:22px;width:248px;height:18px;font-size:7px">Name*</div>
    <div class="field" style="left:12px;top:60px;width:248px;height:18px;font-size:7px">Phone*</div>
    <div class="field" style="left:12px;top:98px;width:248px;height:18px;font-size:7px">Email*</div>
    <div class="field" style="left:12px;top:136px;width:248px;height:18px;font-size:7px">Message*</div>
    <div class="send" style="left:12px;top:180px;width:90px;height:26px;font-size:8px">Send Message</div>
    <div class="foot-head" style="left:12px;top:238px;font-size:7.5px">Postal Address</div>
    <div class="foot-text" style="left:12px;top:254px;font-size:7px">18 Wattle Lane<br>Roselands 2196 NSW<br>Australia</div>
    <div class="foot-text" style="left:12px;top:294px;font-size:7px">02 9000 1234<br>Email: hello@tinyforthouse.com.au</div>
    <div class="social" style="left:12px;top:332px"><span style="width:10px;height:10px"></span><span style="width:10px;height:10px"></span><span style="width:10px;height:10px"></span><span style="width:10px;height:10px"></span><span style="width:10px;height:10px"></span><span style="width:10px;height:10px"></span></div>
    <div class="foot-text" style="left:12px;top:352px;font-size:7px">© Copyright 2018 Tiny Fort House Roselands</div>
  </footer>
</section>

</body>
</html>
```